starlitmanesandtails pet therapy animals

I would like a business card to genarate posative emotions within people. My program has been running in a retirement village for over 5 years I work with residents and family members. My dogs work in palative care and are a great support to family members at the end stage. I also support the families and friends at furnerals when needed to dogs are always with me. Starlitmanes started with the death of my first therapy dog Milo there was such an out cry of grief within the town and retirement village that he had his own furneral The hooves came into it when I was donated a beautiful Miniature horse for the pet therapy program with great results. I now need something very special as a business card. Eg Angelwings my dogs are King Charles Cavaliers so with what I have described can you create something beautiful to acknowledge to work I do and promote it more.

Reason: The reason I have extended the deadline to give other designers a chance to look at the job. So far I have 3 designs. I am hoping to get a few more.

Industry/Entity Type

Town

Contact Information for Business Card

Starlitmanesandtails pet therapy animals
Rosalind Varga
E-mail starlitmanesandtails@quellnet.com
Mobile 0417650382
Pet therapy animals give unconditional love to the aged and disabled.

Font styles to use
Decorative

Colors

Designer to choose colors to be used in the design.

Requirements
Nice to have
• angelwings a King Charles Cavalier tan and white with angel wings and a horse with angel wings

```html
<!DOCTYPE html>
<html lang="en">
<head>
<meta charset="utf-8">
<title>Starlit Manes and Tails – Business Card</title>
<link rel="stylesheet" href="https://fonts.googleapis.com/css2?family=Arimo:wght@400;700&family=Cinzel:wght@500;700&display=swap">
<style>
  :root {
    --page: #ecebe6;
    --sky: #a9e3f3;
    --sky-band: #3d9fdb;
    --ink: #111111;
    --sun: #fde102;
    --mist: #fbf6d8;
    --feather-light: #eef1f2;
    --feather-mid: #c9d0d4;
    --feather-dark: #9aa5ab;
    --halo-pink: #e7c3dd;
    --halo-blue: #b9c9f0;
  }
  * { margin: 0; padding: 0; box-sizing: border-box; }
  html, body {
    width: 1200px; height: 900px; overflow: hidden;
    background: var(--page);
    font-family: "Arimo", Arial, sans-serif;
    color: var(--ink);
  }
  .canvas {
    position: relative; width: 1200px; height: 900px;
    display: flex; flex-direction: column; align-items: center; justify-content: center; gap: 40px;
  }
  .card {
    position: relative; width: 640px; height: 366px; overflow: hidden;
    box-shadow: 0 10px 26px rgba(0,0,0,.22);
  }
  /* front */
  .card--front {
    background: var(--sky);
    border-top: 14px solid var(--sky-band);
    border-bottom: 14px solid var(--sky-band);
    text-align: center;
  }
  .emblem {
    position: absolute; left: 50%; top: 28px; transform: translateX(-50%);
    width: 196px; height: 120px; border-radius: 50%;
    background: radial-gradient(ellipse at 50% 55%, #ffffff 0%, var(--halo-pink) 45%, var(--halo-blue) 100%);
    box-shadow: 0 0 18px 8px rgba(255,255,255,.75);
  }
  .front-text {
    position: absolute; left: 0; right: 0; top: 178px;
    font-family: "Cinzel", "Times New Roman", serif;
    letter-spacing: .1em; line-height: 1.35;
  }
  .business-name { font-size: 20px; font-weight: 700; }
  .tagline { font-size: 17px; font-weight: 500; }
  .mission { font-size: 17px; font-weight: 700; margin-top: 4px; letter-spacing: .06em; }
  /* back */
  .card--back { background: var(--sun); }
  .mist {
    position: absolute; left: 0; right: 0; bottom: 0; height: 150px;
    background: linear-gradient(180deg, rgba(251,246,216,0) 0%, rgba(251,246,216,.85) 50%, rgba(251,246,216,.6) 100%);
  }
  .mist--right {
    position: absolute; right: 0; top: 150px; width: 240px; height: 130px;
    background: radial-gradient(ellipse at 70% 60%, rgba(251,246,216,.9) 0%, rgba(251,246,216,0) 70%);
  }
  .pegasus {
    position: absolute; left: 70px; top: 18px; width: 420px; height: 200px;
    border-radius: 50%;
    background: radial-gradient(ellipse at 55% 55%, var(--feather-light) 0%, var(--feather-mid) 40%, var(--feather-dark) 62%, rgba(154,165,171,0) 72%);
  }
  .contact {
    position: absolute; left: 26px; bottom: 26px;
    font-size: 20px; line-height: 1.4;
  }
</style>
</head>
<body>
<main class="canvas">
  <section class="card card--front">
    <div class="emblem" role="img" aria-label="Tan and white King Charles Cavalier with angel wings on a pastel sky"></div>
    <div class="front-text">
      <p class="business-name">STARLIT MANES AND TAILS</p>
      <p class="tagline">Pet Therapy Animals</p>
      <p class="mission">Give unconditional Love to the aged and disabled.</p>
    </div>
  </section>

  <section class="card card--back">
    <div class="mist"></div>
    <div class="mist--right"></div>
    <div class="pegasus" role="img" aria-label="White winged horse rearing with wings spread wide"></div>
    <div class="contact">
      <p>Name: ROSALIND VARGA</p>
      <p>Email: starlitmanesandtails@quellnet.com</p>
      <p>Mobile: 0417650382</p>
    </div>
  </section>
</main>
</body>
</html>
```